Design eBook Cover for Homeowner Association (HOA) book

We need a cover design for an eBook entitled "The Civic Panel Volunteer's Primer: Self-Direction Hints and Sound Routines".

Title: The Civic Panel Volunteer's Primer

Subtitle: Self-Direction Hints and Sound Routines

Name of Author: Gary Pellston, CMA

Style: Professional Guide

Testimonial: "This book is an indispensable tool for anyone on an HOA board. The expert advice and practical approach in 'The Civic Panel Volunteer's Primer' have made a world of difference in our community. Every board member should have a copy!"
— Wanda Orr, HOA Board President

I have uploaded a file as design inspiration but not locked into the colors or look. Just want a clean, professional looking cover.

Target Market(s)

Board members of HOAs (Homeowners associations) in the United States

Industry/Entity Type

Real Estate, HOA

Requirements
Must have
• Clean, professional appearance that conveys authority

```html
<!DOCTYPE html>
<html lang="en">
<head>
<meta charset="utf-8">
<title>The Civic Panel Volunteer's Primer — Cover</title>
<link rel="stylesheet" href="https://fonts.googleapis.com/css2?family=Bebas+Neue&family=Barlow+Condensed:wght@300;500&display=swap">
<style>
  :root {
    --cover-red: #ec002f;
    --accent-yellow: #fbcf14;
    --ink-white: #ffffff;
    --page-bg: #f4f4f4;
    --house-cream: #f5ecd8;
    --house-cream-dark: #e4d6b8;
  }
  html, body {
    margin: 0;
    padding: 0;
    width: 1200px;
    height: 1200px;
    overflow: hidden;
    background: var(--page-bg);
  }
  .cover {
    position: absolute;
    left: 249px;
    top: 74px;
    width: 701px;
    height: 1051px;
    background: var(--cover-red);
    color: var(--ink-white);
    text-align: center;
    overflow: hidden;
  }
  .subtitle {
    position: absolute;
    top: 52px;
    left: 0;
    right: 0;
    margin: 0;
    font-family: "Bebas Neue", sans-serif;
    font-size: 27px;
    letter-spacing: 2.4px;
    color: var(--accent-yellow);
    white-space: nowrap;
  }
  .title {
    position: absolute;
    top: 100px;
    left: 0;
    right: 0;
    margin: 0;
    font-family: "Bebas Neue", sans-serif;
    font-weight: 400;
    white-space: nowrap;
  }
  .title span {
    display: block;
    line-height: 0.86;
  }
  .title .line-one { font-size: 118px; color: var(--ink-white); }
  .title .line-two { font-size: 146px; color: var(--accent-yellow); }
  .title .line-three { font-size: 190px; color: var(--ink-white); }
  .houses-art {
    position: absolute;
    left: 30px;
    top: 594px;
    width: 624px;
    height: 183px;
    border-radius: 6px;
    background: linear-gradient(180deg, var(--house-cream) 0%, var(--house-cream-dark) 100%);
  }
  .testimonial {
    position: absolute;
    top: 838px;
    left: 70px;
    right: 70px;
    margin: 0;
    font-family: "Barlow Condensed", sans-serif;
    font-weight: 300;
    font-size: 18.5px;
    line-height: 23px;
    color: var(--ink-white);
  }
  .testimonial cite {
    font-style: normal;
    font-weight: 500;
    color: var(--accent-yellow);
  }
  .author {
    position: absolute;
    top: 948px;
    left: 0;
    right: 0;
    margin: 0;
    font-family: "Bebas Neue", sans-serif;
    font-size: 62px;
    letter-spacing: 4px;
    color: var(--ink-white);
    white-space: nowrap;
  }
</style>
</head>
<body>
  <main class="cover">
    <p class="subtitle">Self-Direction Hints and Sound Routines</p>
    <h1 class="title">
      <span class="line-one">THE CIVIC PANEL</span>
      <span class="line-two">VOLUNTEER'S</span>
      <span class="line-three">PRIMER</span>
    </h1>
    <div class="houses-art" role="img" aria-label="Row of four small model houses in cream with blue windows and brown doors"></div>
    <blockquote class="testimonial">
      This book is an indispensable tool for anyone on an HOA board. The expert advice and practical approach in 'The Civic Panel Volunteer's Primer' have made a world of difference in our community. Every board member should have a copy! <cite>— Wanda Orr, HOA Board President</cite>
    </blockquote>
    <p class="author">GARY PELLSTON, CMA</p>
  </main>
</body>
</html>
```